Business cards

We need business cards for the logo that you designed for our company. Something simple and clean.

Target Market(s)

Homeowners/ people looking for construction work

Industry/Entity Type

Construction

Contact Information for Business Card

Name: Dana Holbrit, Number: 602-547-9164, Email: HolbritBuildingGroup@mailvesta.com ROC# 846203

Font styles to use
Serif

Colors

Designer to choose colors to be used in the design.

Requirements
Must have
• On one side of the card I would like to be all of the personal information I have put above along with the company logo that I have attached.
• On the other side of the card I would like the top half of the card to be the logo and then on the bottom half I would like to have the areas of construction we focus on along with an icon that represents it like the picture I have attached.
• Areas we focus on:
• Roofing, Kitchen and bath Remodel, Water Damage, Storm Damage, Fire Damage, Insurance Specialist
• If we could arrange those in alphabetical order.
Nice to have
• I have added 2 company logos a colorful one and a black one it would be nice to see a couple different options the black logo to be more simple and sleek and the colorful logo to be more colorful

```html
<!DOCTYPE html>
<html lang="en">
<head>
<meta charset="utf-8">
<title>Holbrit Building Group — Business Cards</title>
<link rel="stylesheet" href="https://fonts.googleapis.com/css2?family=Source+Serif+4:wght@400;600;700;800&display=swap">
<style>
  :root {
    --navy: #0b2a63;
    --white: #ffffff;
    --muted-white: #d5dcea;
    --pin: #8fa3c4;
    --backdrop: #e9e6e1;
    --fire: #f29a1f;
    --insurance: #3f6fb5;
    --kitchen: #7fb7c4;
    --roofing: #b5533c;
    --storm: #7d7f84;
    --water: #6fa8dc;
    --text-font: "Source Serif 4", Georgia, serif;
  }
  * { box-sizing: border-box; margin: 0; padding: 0; }
  html, body { width: 1200px; height: 1200px; overflow: hidden; }
  body {
    background: var(--backdrop);
    font-family: var(--text-font);
    position: relative;
  }
  .card {
    position: absolute;
    left: 120px;
    width: 960px;
    height: 548px;
    overflow: hidden;
    box-shadow: 0 6px 18px rgba(0,0,0,0.18);
  }

  /* Shared brand line */
  .brand {
    position: absolute;
    display: flex;
    align-items: center;
    color: var(--navy);
    font-weight: 700;
    letter-spacing: 0.04em;
    white-space: nowrap;
  }
  .brand-mark { background: var(--navy); flex: none; }

  /* Front side */
  .card-front { top: 36px; background: var(--navy); }
  .front-wave { position: absolute; inset: 0; width: 100%; height: 100%; }
  .card-front .brand { right: 60px; top: 118px; font-size: 30px; gap: 16px; }
  .card-front .brand-mark { width: 42px; height: 42px; }
  .holder { position: absolute; left: 72px; top: 232px; color: var(--white); }
  .holder-name { font-size: 42px; font-weight: 700; letter-spacing: 0.01em; line-height: 1.1; }
  .holder-role { font-size: 24px; font-weight: 400; color: var(--muted-white); margin-top: 10px; }
  .licence {
    position: absolute; left: 76px; top: 382px;
    color: var(--white); font-size: 24px; font-weight: 700; letter-spacing: 0.12em;
  }
  .contact-list { position: absolute; left: 76px; top: 430px; list-style: none; color: var(--white); }
  .contact-item { display: flex; align-items: center; gap: 10px; font-size: 22px; line-height: 1.5; }
  .contact-icon { width: 22px; height: 22px; flex: none; }

  /* Back side */
  .card-back { top: 616px; background: var(--white); }
  .card-back .brand { left: 0; right: 0; top: 98px; justify-content: center; font-size: 50px; gap: 24px; }
  .card-back .brand-mark { width: 62px; height: 62px; }
  .services {
    position: absolute; left: 0; right: 0; bottom: 0; height: 288px;
    background: var(--navy);
    display: flex; justify-content: space-between; padding: 28px 24px 0;
    list-style: none;
  }
  .service { width: 150px; display: flex; flex-direction: column; align-items: center; }
  .service-pin { width: 110px; height: 148px; }
  .service-label {
    margin-top: 10px; color: var(--white); text-align: center;
    font-size: 17px; font-weight: 700; line-height: 1.3; white-space: nowrap;
  }
  .service-label span { display: block; }
</style>
</head>
<body>

  <section class="card card-front" aria-label="Business card front">
    <svg class="front-wave" viewBox="0 0 960 548" preserveAspectRatio="none" aria-hidden="true">
      <path d="M300 0 C 360 190, 560 330, 960 300 L 960 0 Z" fill="#ffffff"/>
    </svg>
    <div class="brand"><span class="brand-mark"></span>HOLBRIT BUILDING GROUP</div>
    <div class="holder">
      <p class="holder-name">DANA HOLBRIT</p>
      <p class="holder-role">Manager</p>
    </div>
    <p class="licence">ROC# 846203</p>
    <ul class="contact-list">
      <li class="contact-item">
        <svg class="contact-icon" viewBox="0 0 22 22" aria-hidden="true"><rect x="6" y="2" width="10" height="18" rx="1.5" fill="none" stroke="#fff" stroke-width="1.6"/></svg>
        602-547-9164
      </li>
      <li class="contact-item">
        <svg class="contact-icon" viewBox="0 0 22 22" aria-hidden="true"><rect x="2" y="5" width="18" height="12" fill="none" stroke="#fff" stroke-width="1.6"/><path d="M2 5 L11 12 L20 5 M2 17 L9 11 M20 17 L13 11" fill="none" stroke="#fff" stroke-width="1.4"/></svg>
        HolbritBuildingGroup@mailvesta.com
      </li>
    </ul>
  </section>

  <section class="card card-back" aria-label="Business card back">
    <div class="brand"><span class="brand-mark"></span>HOLBRIT BUILDING GROUP</div>
    <ul class="services">
      <li class="service">
        <svg class="service-pin" viewBox="0 0 124 166">
          <path d="M62 166 L12 96 A62 62 0 1 1 112 96 Z" fill="var(--pin)"/>
          <circle cx="62" cy="62" r="46" fill="#fff"/>
          <circle cx="62" cy="62" r="26" fill="var(--fire)" role="img" aria-label="Flame icon"/>
        </svg>
        <p class="service-label"><span>FIRE</span><span>Damage</span></p>
      </li>
      <li class="service">
        <svg class="service-pin" viewBox="0 0 124 166">
          <path d="M62 166 L12 96 A62 62 0 1 1 112 96 Z" fill="var(--pin)"/>
          <circle cx="62" cy="62" r="46" fill="#fff"/>
          <circle cx="62" cy="62" r="26" fill="var(--insurance)" role="img" aria-label="Insurance shield icon"/>
        </svg>
        <p class="service-label"><span>INSURANCE</span><span>Specialist</span></p>
      </li>
      <li class="service">
        <svg class="service-pin" viewBox="0 0 124 166">
          <path d="M62 166 L12 96 A62 62 0 1 1 112 96 Z" fill="var(--pin)"/>
          <circle cx="62" cy="62" r="46" fill="#fff"/>
          <circle cx="62" cy="62" r="26" fill="var(--kitchen)" role="img" aria-label="Kitchen and bath faucet icon"/>
        </svg>
        <p class="service-label"><span>KITCHEN &amp; BATH</span><span>Remodel</span></p>
      </li>
      <li class="service">
        <svg class="service-pin" viewBox="0 0 124 166">
          <path d="M62 166 L12 96 A62 62 0 1 1 112 96 Z" fill="var(--pin)"/>
          <circle cx="62" cy="62" r="46" fill="#fff"/>
          <circle cx="62" cy="62" r="26" fill="var(--roofing)" role="img" aria-label="Roof icon"/>
        </svg>
        <p class="service-label"><span>ROOFING</span></p>
      </li>
      <li class="service">
        <svg class="service-pin" viewBox="0 0 124 166">
          <path d="M62 166 L12 96 A62 62 0 1 1 112 96 Z" fill="var(--pin)"/>
          <circle cx="62" cy="62" r="46" fill="#fff"/>
          <circle cx="62" cy="62" r="26" fill="var(--storm)" role="img" aria-label="Storm cloud icon"/>
        </svg>
        <p class="service-label"><span>STORM</span><span>Damage</span></p>
      </li>
      <li class="service">
        <svg class="service-pin" viewBox="0 0 124 166">
          <path d="M62 166 L12 96 A62 62 0 1 1 112 96 Z" fill="var(--pin)"/>
          <circle cx="62" cy="62" r="46" fill="#fff"/>
          <circle cx="62" cy="62" r="26" fill="var(--water)" role="img" aria-label="Water drop icon"/>
        </svg>
        <p class="service-label"><span>WATER</span><span>Damage</span></p>
      </li>
    </ul>
  </section>

</body>
</html>
```